Australian Civil Construction, Quarry & Mining Services needs a business card

We need a business card designed for our Civil Construction, Quarry & Mining Services based in the country in Australia.
Our Company Brindle Earthworks provide innovate solutions for infrastructure, agricultural and mining (aggregate, sand, roadbase) industry.
We would like our business cards to be double sided
Front of card: black background or something that resembles our business colours. (it doesn't have to be black we are open to options)
- Company name - Brindle Earthworks
- Either our logo or some sort of icon/picture that resembles our business
- Website - https://brindleearthworks-example.com.au/
- We will have a number of different names, positions descriptions, phone numbers and emails on separate cards for each of our managers/directors

```html
<!DOCTYPE html>
<html lang="en">
<head>
<meta charset="utf-8">
<title>Brindle Earthworks – Business Card</title>
<link rel="stylesheet" href="https://fonts.googleapis.com/css2?family=Lato:wght@400;700;900&display=swap">
<style>
  :root {
    --page-bg: #e9e6e3;
    --card-dark: #1f1416;
    --brand-orange: #fd8217;
    --text-light: #ffffff;
    --seal-light: #e4e3e4;
    --seal-text: #1f1416;
  }
  * { margin: 0; padding: 0; box-sizing: border-box; }
  html, body {
    width: 1200px;
    height: 900px;
    overflow: hidden;
    background: var(--page-bg);
    font-family: "Lato", Arial, sans-serif;
  }
  .canvas {
    position: relative;
    width: 1200px;
    height: 900px;
  }
  .business-card {
    position: absolute;
    left: 100px;
    top: 140px;
    width: 1000px;
    height: 620px;
    background: var(--card-dark);
    overflow: hidden;
    box-shadow: 0 18px 40px rgba(0,0,0,0.18);
  }
  .accent-band {
    position: absolute;
    left: 714px;
    top: 0;
    width: 286px;
    height: 100%;
    background: var(--brand-orange);
  }
  .brand-seal {
    position: absolute;
    left: 456px;
    top: 49px;
    width: 518px;
    height: 518px;
    border-radius: 50%;
    background: var(--seal-light);
    display: flex;
    align-items: center;
    justify-content: center;
    text-align: center;
  }
  .brand-name {
    font-weight: 900;
    font-size: 46px;
    line-height: 1.1;
    color: var(--seal-text);
    letter-spacing: 1px;
    text-transform: uppercase;
  }
  .person {
    position: absolute;
    left: 46px;
    top: 82px;
  }
  .person-name {
    font-weight: 900;
    font-size: 39px;
    color: var(--brand-orange);
    letter-spacing: 0.5px;
    line-height: 1.1;
    text-transform: uppercase;
  }
  .person-role {
    font-weight: 400;
    font-size: 29px;
    color: var(--text-light);
    line-height: 1.2;
  }
  .address {
    position: absolute;
    left: 46px;
    top: 332px;
    font-size: 26px;
    line-height: 36px;
    color: var(--text-light);
    font-style: normal;
  }
  .contact-list {
    position: absolute;
    left: 46px;
    top: 424px;
    list-style: none;
  }
  .contact-item {
    display: flex;
    align-items: center;
    height: 39px;
    font-size: 26px;
    letter-spacing: -0.2px;
    color: var(--text-light);
    white-space: nowrap;
  }
  .contact-icon {
    width: 28px;
    height: 28px;
    margin-right: 9px;
    flex: none;
  }
</style>
</head>
<body>
<main class="canvas">
  <section class="business-card" aria-label="Brindle Earthworks business card">
    <div class="accent-band"></div>

    <div class="brand-seal">
      <span class="brand-name">Brindle<br>Earthworks</span>
    </div>

    <header class="person">
      <h1 class="person-name">Marcus Hale</h1>
      <p class="person-role">Managing Director</p>
    </header>

    <address class="address">
      421, Address line here<br>
      Country Name, 45452
    </address>

    <ul class="contact-list">
      <li class="contact-item">
        <svg class="contact-icon" viewBox="0 0 24 24" aria-hidden="true">
          <path fill="var(--brand-orange)" d="M6.6 10.8a15.1 15.1 0 0 0 6.6 6.6l2.2-2.2a1 1 0 0 1 1-.25 11.4 11.4 0 0 0 3.6.57 1 1 0 0 1 1 1V20a1 1 0 0 1-1 1A17 17 0 0 1 3 4a1 1 0 0 1 1-1h3.5a1 1 0 0 1 1 1c0 1.250.2 2.450.57 3.6a1 1 0 0 1-.25 1z"/>
          <path fill="none" stroke="var(--brand-orange)" stroke-width="1.6" stroke-linecap="round" d="M14 3.5a7 7 0 0 1 6.5 6.5M14 7a3.5 3.5 0 0 1 3 3"/>
        </svg>
        044-987 650 321
      </li>
      <li class="contact-item">
        <svg class="contact-icon" viewBox="0 0 24 24" aria-hidden="true">
          <rect x="2" y="5" width="20" height="14" fill="var(--brand-orange)"/>
          <path fill="none" stroke="var(--card-dark)" stroke-width="1.5" d="M2 5l10 8 10-8M2 19l7.5-7M22 19l-7.5-7"/>
        </svg>
        info@brindlemail.com
      </li>
      <li class="contact-item">
        <svg class="contact-icon" viewBox="0 0 24 24" aria-hidden="true">
          <g fill="none" stroke="var(--brand-orange)" stroke-width="1.8">
            <circle cx="12" cy="12" r="9.5"/>
            <ellipse cx="12" cy="12" rx="4.2" ry="9.5"/>
            <path d="M2.5 12h19M4 7h16M4 17h16"/>
          </g>
        </svg>
        www.brindleearthworks-example.com.au
      </li>
    </ul>
  </section>
</main>
</body>
</html>
```